KESTREL Posters

We are a very large, international law firm. We seek a collection of posters (approximately 4) as part of a communications campaign about the upgrade of the firm’s computer systems from Deskline 2003 to Deskline 2010 (Mailvane, Scribo, Tabulo and Slidecraft). The audience for the campaign is made up of lawyers, legal secretaries, paralegals and administrative staff. The corporate environment is high-powered professionals focused on delivering superior client service.
Comprehensive training programs will be made available to help users make the transition from Deskline 2003 to Deskline 2010. We anticipate it being easier for the users to successfully transition if they take advantage of the training opportunities. Training for secretaries is mandatory, but training for lawyers is optional.
The posters should be designed to send a positive message about the upgraded system and encourage lawyers and secretaries to take advantage of the training opportunities. We have a “logo/tagline” for this initiative (attached) and we would like the posters to relate to the tagline, “KESTREL: Kits Built for Every Daily Task”.

Reason: Would like to make sure there is sufficient time for designers to receive and respond to my latest feedback.

Reason: Extending to allow for enough time to update after my last feedback.

Target Market(s)

Attorneys who are either technophobic or uninterested in computers and secretaries who are fearful of computers and change generally.

Industry/Entity Type

Communications

Requirements
Must have
• Positive message.
Excitement.
Professional Look and Feel.
Nice to have
• The posters should relate to the tagline “KESTREL: Kits Built for Every Daily Task”. See the attached file for what this looks like. The poster does not need to specifically mention Deskline or Deskline 2010 or technology.

Your slider seems prone to misinterpretation. To clarify, the following describes the style that illustrates what the poster should communicate:
Elegant/Bold 50/50
Playful/Serious 60/40
Traditional/Modern 50/50
Personable/Professional 30/70
Feminine/Masculine 50/50
Colorful/Conservative 30/70
Economical/Upmarket 20/80
Playful-Professional-Conservative-Upmarket are more heavily weighted.
Should not have
• The concept should not focus on “change” – change makes people anxious and one of our goals with this campaign is to reduce anxiety about the change to Deskline 2010.
The concept should also avoid negative comparisons/images/references to our current suite of tools (Deskline 2003).

```html
<!DOCTYPE html>
<html lang="en">
<head>
<meta charset="utf-8">
<title>KESTREL — Kits Built for Every Daily Task</title>
<link rel="stylesheet" href="https://fonts.googleapis.com/css2?family=Questrial&display=swap">
<style>
  :root {
    --blue-glow: #3c9be0;
    --blue-mid: #1768b4;
    --blue-deep: #0b3f82;
    --blue-edge: #082f66;
    --white: #ffffff;
    --tab-top: #ffffff;
    --tab-bottom: #dcdfe6;
    --wordmark: #3b3a44;
    --tagline: #34497c;
    --mark: #2c4a8c;
    --ball-light: #e0702f;
    --ball-dark: #8e3210;
  }
  html, body {
    margin: 0;
    padding: 0;
    overflow: hidden;
    background: var(--blue-edge);
  }
  .poster {
    position: relative;
    width: 848px;
    height: 1200px;
    overflow: hidden;
    font-family: "Questrial", "Helvetica Neue", Arial, sans-serif;
    color: var(--white);
    background:
      radial-gradient(ellipse 520px 560px at 410px 250px, var(--blue-glow) 0%, var(--blue-mid) 45%, var(--blue-deep) 78%, var(--blue-edge) 100%);
  }
  .hero-ball {
    position: absolute;
    left: 192px;
    top: 50px;
    width: 428px;
    height: 428px;
    border-radius: 50%;
    background: radial-gradient(circle at 40% 35%, var(--ball-light) 0%, #c2511d 55%, var(--ball-dark) 100%);
  }
  .hero-ball-shadow {
    position: absolute;
    left: 250px;
    top: 500px;
    width: 310px;
    height: 26px;
    border-radius: 50%;
    background: radial-gradient(ellipse at center, rgba(5,25,60,0.75) 0%, rgba(5,25,60,0) 70%);
  }
  .headline {
    position: absolute;
    left: 0;
    width: 100%;
    top: 620px;
    margin: 0;
    text-align: center;
    font-weight: 400;
    line-height: 1;
    letter-spacing: 1px;
  }
  .headline-small {
    display: block;
    font-size: 48px;
  }
  .headline-large {
    display: block;
    font-size: 62px;
    margin-top: 10px;
  }
  .call-to-action {
    position: absolute;
    left: 0;
    width: 100%;
    top: 810px;
    margin: 0;
    text-align: center;
    font-size: 31px;
    line-height: 43px;
  }
  .brand-tab {
    position: absolute;
    left: 143px;
    top: 1047px;
    width: 577px;
    height: 170px;
    border-radius: 90px 90px 0 0;
    background: linear-gradient(to bottom, var(--tab-top) 0%, var(--tab-top) 45%, var(--tab-bottom) 100%);
    box-shadow: 0 -4px 18px rgba(0,20,60,0.35);
  }
  .brand-mark {
    position: absolute;
    left: 118px;
    top: 48px;
    width: 48px;
    height: 48px;
    border-radius: 50%;
    background: var(--mark);
  }
  .brand-name {
    position: absolute;
    left: 176px;
    top: 38px;
    margin: 0;
    font-size: 52px;
    line-height: 1;
    letter-spacing: 3px;
    color: var(--wordmark);
    font-weight: 400;
  }
  .brand-tagline {
    position: absolute;
    left: 178px;
    top: 101px;
    margin: 0;
    font-size: 22px;
    line-height: 1;
    color: var(--tagline);
    letter-spacing: 0.5px;
  }
</style>
</head>
<body>
  <main class="poster">
    <div class="hero-ball-shadow"></div>
    <div class="hero-ball" role="img" aria-label="Photograph of an orange basketball glowing against the blue background"></div>

    <h1 class="headline">
      <span class="headline-small">KITS BUILT FOR</span>
      <span class="headline-large">EVERY DAILY TASK</span>
    </h1>

    <p class="call-to-action">Take advantage<br>of the training opportunities</p>

    <footer class="brand-tab">
      <span class="brand-mark"></span>
      <p class="brand-name">KESTREL</p>
      <p class="brand-tagline">kits built for every daily task</p>
    </footer>
  </main>
</body>
</html>
```